New Motorcycle Model (Vireo 2019) Poster Design with highlighted features.

Poster : The dimension is 80cm(W) x 120cm(H)
We are a leading company for manufacturing Motorcycles based in Egypt. We 'd like to design a 80x180cm poster to highlight the new enhancements introduced in VIREO model 2019.
If we 'd like to break down the design into different sections will be:
- 2 Company logos (BRUMK & TORVELIN)
- The motorcycle portrait.
- The featured motorcycle parts with some space to write small description for each part.
- Header: MODRENI VIREO 150 (K72) 2019 Features.
- A line for a greetings from the company.
P.S:It's preferred to have the all the text easily editable at the poster because it will be in another Language in the final revision.
Target Market(s)
Economical Motorcycle Buyers
Look and feel
Each slider illustrates characteristics of the customer's brand and the style your logo design should communicate.

```html
<!DOCTYPE html>
<html lang="en">
<head>
<meta charset="utf-8">
<title>Modreni Vireo 150 (K72) 2019 Poster</title>
<link rel="stylesheet" href="https://fonts.googleapis.com/css2?family=Audiowide&family=Roboto:wght@400;700&display=swap">
<style>
  :root {
    --bg: #e9ecef;
    --poster-dark: #2b2b2d;
    --poster-darker: #1c1c1e;
    --red: #d3181e;
    --red-deep: #9e0d12;
    --white: #ffffff;
    --grey-band: #b9bcc0;
    --text-dark: #222222;
  }
  html, body { margin: 0; padding: 0; width: 1200px; height: 1200px; overflow: hidden; background: var(--bg); }
  .poster {
    position: absolute; left: 220px; top: 30px; width: 760px; height: 1140px;
    background: linear-gradient(180deg, var(--poster-dark) 0%, #3a3a3c 55%, var(--poster-darker) 100%);
    overflow: hidden; font-family: 'Roboto', sans-serif;
    box-shadow: 0 6px 24px rgba(0,0,0,.25);
  }
  .decor { position: absolute; inset: 0; }
  .headline {
    position: absolute; left: 30px; top: 70px; width: 700px;
    transform: rotate(-13deg); transform-origin: left top;
    font-family: 'Audiowide', sans-serif; font-style: italic;
  }
  .headline .brand-name, .headline .model-name {
    display: block; color: var(--red); font-size: 76px; line-height: 1;
    -webkit-text-stroke: 3px var(--white); paint-order: stroke fill;
    text-shadow: 3px 3px 0 #000;
  }
  .headline .brand-name { margin-left: 20px; }
  .headline .model-name { margin-left: 190px; }
  .model-code {
    position: absolute; left: 350px; top: 150px; transform: rotate(-13deg);
    font-family: 'Audiowide', sans-serif; color: var(--white); font-size: 64px;
    text-shadow: 2px 2px 0 #000;
  }
  .model-year {
    position: absolute; left: 500px; top: 240px; transform: rotate(-13deg);
    font-family: 'Audiowide', sans-serif; color: var(--red); font-size: 62px;
    -webkit-text-stroke: 2px var(--white); paint-order: stroke fill;
  }
  .star { position: absolute; color: var(--white); font-size: 28px; }
  .bike-photo {
    position: absolute; left: 20px; top: 330px; width: 720px; height: 360px;
    background: radial-gradient(ellipse at 50% 55%, #b21b20 0%, #6c1014 45%, rgba(40,40,42,0) 75%);
    border-radius: 8px;
  }
  .feature {
    position: absolute; width: 160px;
  }
  .feature-photo {
    height: 118px; border: 4px solid var(--red); box-sizing: border-box;
    background: linear-gradient(160deg, #e6e6e6, #8a8a8a);
  }
  .feature-text {
    background: var(--white); margin-top: 10px; padding: 12px 10px;
    color: var(--text-dark); font-size: 11.5px; line-height: 1.45; text-align: center;
    min-height: 120px; box-sizing: border-box;
  }
  .logos { position: absolute; right: 30px; top: 930px; display: flex; gap: 40px; align-items: center; }
  .logo { display: flex; align-items: center; gap: 8px; color: var(--white); font-weight: 700; font-size: 26px; letter-spacing: 1px; }
  .logo-dot { width: 22px; height: 22px; border-radius: 50%; background: var(--white); }
  .footer-bar {
    position: absolute; left: 0; bottom: 0; width: 100%; height: 100px;
    background: linear-gradient(180deg, var(--red), var(--red-deep));
    display: flex; align-items: center; justify-content: space-between; padding: 0 36px; box-sizing: border-box;
    color: var(--poster-darker); font-weight: 700; font-size: 30px;
  }
  .footer-bar .contact { display: flex; align-items: center; gap: 12px; }
</style>
</head>
<body>
<main class="poster">
  <svg class="decor" width="760" height="1140" viewBox="0 0 760 1140" aria-hidden="true">
    <polygon points="0,260 760,40 760,90 0,330" fill="#8b1116" opacity=".55"/>
    <polygon points="300,120 760,0 760,20 330,135" fill="#d3181e" opacity=".7"/>
    <polygon points="0,220 540,60 560,70 0,240" fill="#d3181e" opacity=".5"/>
    <polygon points="0,860 760,640 760,700 0,930" fill="#b9bcc0"/>
    <polygon points="0,900 760,680 760,690 0,915" fill="#ffffff" opacity=".6"/>
    <polygon points="0,1000 420,960 430,975 0,1020" fill="#d3181e"/>
    <polygon points="0,1030 360,1000 370,1012 0,1045" fill="#d3181e" opacity=".7"/>
  </svg>

  <h1 class="headline">
    <span class="brand-name">MODRENI</span>
    <span class="model-name">VIREO</span>
  </h1>
  <div class="model-code">150 (K72)</div>
  <div class="model-year">2019</div>
  <span class="star" style="left:690px;top:225px">★</span>
  <span class="star" style="left:452px;top:330px">★</span>

  <div class="bike-photo" role="img" aria-label="Studio photo of the red Vireo 150 motorcycle, side view"></div>

  <section class="feature" style="left:22px;top:730px">
    <div class="feature-photo" role="img" aria-label="Close-up of the engine block"></div>
    <p class="feature-text">Reinforced engine block with improved cooling fins delivers smoother power and longer service life on daily city rides.</p>
  </section>
  <section class="feature" style="left:204px;top:700px">
    <div class="feature-photo" role="img" aria-label="Close-up of footrest and gear lever"></div>
    <p class="feature-text">New footrest and gear lever layout gives a more relaxed riding position and easier shifting in heavy traffic.</p>
  </section>
  <section class="feature" style="left:386px;top:670px">
    <div class="feature-photo" role="img" aria-label="Close-up of front fender and wheel"></div>
    <p class="feature-text">Stronger front fender and alloy wheel design keep the bike clean, stable and safe on rough roads.</p>
  </section>
  <section class="feature" style="left:568px;top:640px">
    <div class="feature-photo" role="img" aria-label="Close-up of the twin gauge dashboard"></div>
    <p class="feature-text">Clear twin gauge dashboard shows speed and engine revs at a glance, day or night, for confident riding.</p>
  </section>

  <div class="logos">
    <div class="logo"><span class="logo-dot"></span>BRUMK</div>
    <div class="logo"><span class="logo-dot"></span>TORVELIN</div>
  </div>

  <footer class="footer-bar">
    <div class="contact">
      <svg width="28" height="28" viewBox="0 0 24 24" aria-hidden="true"><path fill="#1c1c1e" d="M6.6 10.8a15.1 15.1 0 0 0 6.6 6.6l2.2-2.2a1 1 0 0 1 1-.25 11.4 11.4 0 0 0 3.6.57 1 1 0 0 1 1 1V20a1 1 0 0 1-1 1A17 17 0 0 1 3 4a1 1 0 0 1 1-1h3.5a1 1 0 0 1 1 1c0 1.25.2 2.45.57 3.6a1 1 0 0 1-.25 1z"/></svg>
      <span>1 555 014 27</span>
    </div>
    <svg width="44" height="44" viewBox="0 0 24 24" aria-hidden="true"><path fill="#1c1c1e" d="M12 8a4 4 0 1 0 0 8 4 4 0 0 0 0-8zm9 5.5v-3l-2.3-.5a7 7 0 0 0-.7-1.7l1.3-2-2.1-2.1-2 1.3a7 7 0 0 0-1.7-.7L13.5 3h-3l-.5 2.3a7 7 0 0 0-1.7.7l-2-1.3-2.1 2.1 1.3 2a7 7 0 0 0-.7 1.7L3 10.5v3l2.3.5c.15.6.4 1.2.7 1.7l-1.3 2 2.1 2.1 2-1.3c.5.3 1.1.55 1.7.7l.5 2.3h3l.5-2.3a7 7 0 0 0 1.7-.7l2 1.3 2.1-2.1-1.3-2c.3-.5.55-1.1.7-1.7z"/></svg>
    <span class="website">www.vireoride.com</span>
  </footer>
</main>
</body>
</html>
```